The Hidden Harvest Summit (Poster or Color Flyer)

Unique and not too traditional design with Wording:
The Hidden Harvest Summit: The Deeper Message of God's Relentless Love
Friday Aug. 5 - Sunday the 7th
Denver 2016
www.TheHarvestSummitEvent.com
Updates
Project Deadline Extended
Reason: Our first experience with this type of design service was with 42Sketchery, and we received 140 designs within a week.
We received only 2 designers submissions by our first 5 days with Artisan Pool. We received an email that our time would be extended, which is much appreciated. The last 24 hours has brought in several new designs - which is great. However, we have a team of reviewers on our end - and due to Christmas break, will not be able to make a decision until January 4 or 5.
Can our deadline be moved to January 5? (at no charge?)
THANKS,
Glen
Target Market(s)
General public. Professors. Pastors.
Requirements
Must have
- Basic info above.
Nice to have
- Subtle verses tucked into the graphics
- See www.TheKQRs.com for some of these,
- such as Romans 11:32, 1 John 2:2, 1 Timothy 4:10, John 12:32
Should not have
- Typical religious appearance.

```html
<!DOCTYPE html>
<html lang="en">
<head>
<meta charset="utf-8">
<title>The KQRs – The Hidden Harvest Summit</title>
<link rel="stylesheet" href="https://fonts.googleapis.com/css2?family=Cardo:wght@400;700&display=swap">
<style>
  :root {
    --mint: #b9dfc8;
    --navy: #1d4c9c;
    --red: #d9292f;
    --ink: #3a3a36;
    --white: #ffffff;
    --sky-blue: #8fb6e0;
    --sky-red: #e0625f;
  }
  * { margin: 0; padding: 0; box-sizing: border-box; }
  html, body { width: 928px; height: 1200px; overflow: hidden; }
  body { font-family: "Cardo", Georgia, serif; font-weight: 700; }
  .poster {
    position: relative; width: 928px; height: 1200px;
    background: var(--mint); overflow: hidden;
  }
  .header { position: absolute; left: 0; right: 0; text-align: center; line-height: 1.2; white-space: nowrap; }
  .series-title { top: 52px; font-size: 113px; color: var(--navy); letter-spacing: 1px; line-height: 1.1; }
  .series-subtitle { top: 191px; font-size: 64px; color: var(--red); line-height: 1.1; }
  .event-prefix { top: 302px; font-size: 33px; color: var(--ink); }
  .event-name { top: 350px; font-size: 58px; color: var(--navy); }
  .event-tagline { top: 422px; font-size: 33px; color: var(--ink); }
  .event-dates { top: 511px; font-size: 33px; color: var(--ink); line-height: 50px; }
  .event-url { top: 609px; font-size: 32px; color: var(--navy); }
  .skyline {
    position: absolute; left: 0; top: 656px; width: 928px; height: 256px;
    background: linear-gradient(90deg, var(--sky-red) 0%, var(--sky-blue) 30%, var(--sky-red) 55%, var(--sky-blue) 75%, var(--sky-red) 100%);
    opacity: 0.85;
  }
  .verse-band {
    position: absolute; left: 0; top: 912px; width: 928px; height: 288px;
    background: var(--red); color: var(--white); padding: 3px 40px 0 48px;
  }
  .verse { font-size: 17.5px; line-height: 24px; margin-bottom: 16px; }
  .thanks { text-align: center; font-size: 26.5px; line-height: 32px; margin-top: 10px; }
</style>
</head>
<body>
<main class="poster">
  <h1 class="header series-title">The “KQR”s</h1>
  <p class="header series-subtitle">Bible Verses Banned</p>
  <p class="header event-prefix">The Hidden</p>
  <h2 class="header event-name">Harvest Summit :</h2>
  <p class="header event-tagline">The Deeper Message of God's Relentless Love</p>
  <p class="header event-dates">Friday Aug. 5 - Sunday the 7th<br>Denver 2016</p>
  <p class="header event-url">www.TheHarvestSummitEvent.com</p>

  <div class="skyline" role="img" aria-label="Flat illustration of a city skyline with a clock tower, phone box, double-decker bus, buildings, taxi, post box and rain clouds in red, blue and black"></div>

  <section class="verse-band">
    <p class="verse">"For God has consigned ALL to disobedience so that He may have mercy on them ALL." (Romans 11:32)</p>
    <p class="verse">"He is the atoning sacrifice for our sins, and not only for ours but also for the sins of the whole world."<br>(1 John 2:2)</p>
    <p class="verse">"That is why we labor because we trust in the living God who is the savior of all men, especially those<br>who believe." (1 Timothy 4:10)</p>
    <p class="verse">"And I, when I am lifted up from the earth, will draw all people to myself."&nbsp; (John 12:32)</p>
    <p class="thanks">THANKS!!!</p>
  </section>
</main>
</body>
</html>
```